Beauty Clinic Treatment Menu (Lumen Nails & Beauty)

Needing a treatment menu designed for a beauty clinic in Whitianga, New Zealand. Like the colours grey, pink, white.
Elegant, Modern and feminine

Lumen Nails & Beauty
Karen Pell
Room3, 48 Tainui Street
Whitianga
0273816240
Karen.lumen@mailbox.test
lumenbeauty.co.nz

Target Market(s)

Females

Industry/Entity Type

Beauty Salon

Font styles to use
Serif

Colors

Requirements
Must have
• Chatterly and Snapgrid logo

```html
<!DOCTYPE html>
<html lang="en">
<head>
<meta charset="utf-8">
<title>Lumen Nails &amp; Beauty — Treatment Menu</title>
<link href="https://fonts.googleapis.com/css2?family=Libre+Baskerville:wght@700&family=Marcellus&display=swap" rel="stylesheet">
<style>
  :root {
    --grey: #d9d9d9;
    --pink: #e4c5c8;
    --ink: #2a2a2c;
  }
  html, body { margin: 0; padding: 0; overflow: hidden; }
  .menu {
    position: relative;
    width: 1200px;
    height: 933px;
    background: var(--grey);
    color: var(--ink);
    font-family: "Marcellus", serif;
    overflow: hidden;
  }
  .menu__band {
    position: absolute;
    left: 401px;
    top: 0;
    width: 404px;
    height: 933px;
    background: var(--pink);
  }
  .line {
    position: absolute;
    width: 400px;
    margin: 0 0 0 -200px;
    text-align: center;
    transform: translateY(-50%);
    white-space: nowrap;
    line-height: 1.2;
    font-weight: 400;
  }
  .col-nails { left: 203px; }
  .col-facials { left: 600px; }
  .col-waxing { left: 992px; }
  .title {
    font-size: 44px;
    letter-spacing: 20px;
    padding-left: 20px;
  }
  .section {
    font-family: "Libre Baskerville", serif;
    font-weight: 700;
    font-size: 20px;
    letter-spacing: 2.5px;
  }
  .section--large {
    font-size: 22px;
    letter-spacing: 1.5px;
  }
  .subhead {
    font-family: "Libre Baskerville", serif;
    font-weight: 700;
    font-size: 13.5px;
    letter-spacing: 1.6px;
  }
  .item {
    font-size: 14.5px;
    letter-spacing: 1.6px;
  }
  .note {
    font-size: 13.5px;
    letter-spacing: 1.2px;
  }
  sup { font-size: 7px; vertical-align: 6px; }
</style>
</head>
<body>
<main class="menu">
  <div class="menu__band"></div>

  <h1 class="line col-facials title" style="top:71px">MENU</h1>

  <!-- Nails -->
  <div class="line col-nails section" style="top:165px">NAILS</div>
  <div class="line col-nails subhead" style="top:230px">MANICURE</div>
  <div class="line col-nails item" style="top:272px">GEL POLISH | $45</div>
  <div class="line col-nails item" style="top:313px">REGULAR POLISH | $40</div>
  <div class="line col-nails subhead" style="top:375px">PEDICURE</div>
  <div class="line col-nails item" style="top:417px">GEL POLISH | $45</div>
  <div class="line col-nails item" style="top:458px">REGULAR POLISH | $40</div>
  <div class="line col-nails subhead" style="top:520px">LUXURY PEDICURE</div>
  <div class="line col-nails note" style="top:542px">Includes: soak, exfoliation,</div>
  <div class="line col-nails note" style="top:563px">heel rasping and massage</div>
  <div class="line col-nails item" style="top:603px">GEL POLISH | $60</div>
  <div class="line col-nails item" style="top:645px">REGULAR POLISH | $55</div>
  <div class="line col-nails subhead" style="top:686px">REMOVAL &amp; NAIL TIDY | $25</div>
  <div class="line col-nails subhead" style="top:728px">ADD ON</div>
  <div class="line col-nails item" style="top:749px">GEL REMOVAL | $5</div>
  <div class="line col-nails item" style="top:769px">RBX | $5 PER LAYER</div>
  <div class="line col-nails item" style="top:790px">BUILDER BASE GEL | $10</div>
  <div class="line col-nails item" style="top:811px">NAIL ART/GLITTER | SPOA</div>

  <!-- Facials -->
  <div class="line col-facials section" style="top:162px">FACIALS</div>
  <div class="line col-facials subhead" style="top:229px">DEEP CLEANSING FACIAL | $75</div>
  <div class="line col-facials note" style="top:258px">45 minutes</div>
  <div class="line col-facials note" style="top:286px">Removes build up of dead skin cells, leaves the</div>
  <div class="line col-facials note" style="top:307px">skin feeling soft and hydrated.</div>

  <div class="line col-facials subhead" style="top:361px">THERAPEUTIC FACIAL | $105</div>
  <div class="line col-facials note" style="top:390px">60 minutes</div>
  <div class="line col-facials note" style="top:418px">Tailored to suit your skins specific needs.</div>

  <div class="line col-facials subhead" style="top:480px">REJUVENATION FACIAL | $120</div>
  <div class="line col-facials note" style="top:508px">60 minutes</div>
  <div class="line col-facials note" style="top:536px">Active yet gentle treatment that facilitates</div>
  <div class="line col-facials note" style="top:564px">dermal rejuvenation.</div>

  <div class="line col-facials subhead" style="top:626px">35% GLYCOLIC FACIAL | $120</div>
  <div class="line col-facials note" style="top:655px">60 minutes</div>
  <div class="line col-facials note" style="top:683px">Hydrating, deep exfoliation treatment improving</div>
  <div class="line col-facials note" style="top:711px">skin texture and appearance.</div>

  <div class="line col-facials subhead" style="top:773px">DERMAPLANING | $120</div>
  <div class="line col-facials note" style="top:802px">Creates a smooth and radiant skin surface.</div>
  <div class="line col-facials note" style="top:830px">Also removes soft facial hairs.</div>

  <!-- Eyes, face, body -->
  <div class="line col-waxing section" style="top:162px">EYES</div>
  <div class="line col-waxing item" style="top:206px">KUMO LASH LIFT | $115</div>
  <div class="line col-waxing item" style="top:234px">EYEBROW SHAPE | $19</div>
  <div class="line col-waxing item" style="top:262px">EYEBROW TINT | $18</div>
  <div class="line col-waxing item" style="top:290px">EYELASH TINT | $25</div>
  <div class="line col-waxing item" style="top:318px">EYE TRIO | $45</div>

  <div class="line col-waxing section section--large" style="top:365px">FACE</div>
  <div class="line col-waxing item" style="top:403px">LIP | $15</div>
  <div class="line col-waxing item" style="top:431px">CHIN | $15</div>

  <div class="line col-waxing section section--large" style="top:479px">BODY</div>
  <div class="line col-waxing item" style="top:517px">UNDERARM | $20</div>
  <div class="line col-waxing item" style="top:545px">1/2 LEG | $35</div>
  <div class="line col-waxing item" style="top:573px">FULL LEG | $55</div>
  <div class="line col-waxing item" style="top:601px">1/2 ARM | $30</div>
  <div class="line col-waxing item" style="top:630px">FULL ARM | $40</div>
  <div class="line col-waxing item" style="top:658px">BIKINI | $28</div>
  <div class="line col-waxing item" style="top:686px">EXTENDED BIKINI | $38</div>
  <div class="line col-waxing item" style="top:714px">BRAZILIAN (1<sup>ST</sup> TIME) | $65</div>
  <div class="line col-waxing item" style="top:742px">BRAZILIAN (4-6 WEEKS) | $50</div>
  <div class="line col-waxing item" style="top:770px">PATCHES | $5</div>
</main>
</body>
</html>
```